National Teen and Tween Athletic Business Needs Banner Designs for Breast Cancer Awareness Month

We need a series of two to four (2-4) of simple and impactful banners for our website carousel (see www.falconridgeteen.com) in size 901 wide by 444 tall (anything close is ok).

It is for a breast cancer donation we were able to negotiate with our factory just this past Thursday.

If we pre-sell 2500 bras in two weeks we can donate $25,000 to breast cancer research

On Friday a colleague and I separately video’d 10 second messages saying that we worked out a deal with our factory to make 2500 smoothknit sprinter bras, which is one production run, in white with pink. We held up the white/ lime color (see http://www.falconridgeteen.com/bras/the-sprinter.html) (http://www.falconridgeteen.com/catalog/product/gallery/id/248/image/430/pid/273/) and described it would be white with pink and that if we sold 2,500 we could do one production run and donate $25000 to breast cancer research.

I did record a second message that mentioned we would contribute to Maren’s Hub. Dr Maren Tovill worldwide breast cancer specialist at BVT Halworth in North Carolina. Then there is a call to action “lets do it!”

We'd like to make banners for the website.

Designers, we'd appreciate your advice on if we can link or use the video's in one of the carousel banners.

If you want to purchase a photo on pixvault or other photo service, please use it with the watermark on your design and if you are the winner, direct us to the photo and we can buy it.

(The below messaging could be one banner, three or four)

First message:
Starting October 17th:
A two week campaign
To sell 2,500 bras
To raise $25,000 for breast cancer
Let's do it!

I’d like to do a Falconridge Honor and Memory wall banner where-whether you buy a bra or not, folks can list someone to honor or remember. One of our investors, Maren Quobel, is a breast cancer survivor and our finance person, Judy Perrowe’s mother, Rosa Telvic, passed away in 1990 at age 51 from breast cancer. We would like to be able to keep adding names to this and update it daily.

Target Market(s)

Girls ages 10-17 and their parents and coaches. Our customer is a serious athletic girl, think of Brinna Holloway from Ember Trials and Tess Rudd, soccer star.

Industry/Entity Type

Business

Font styles to use
Sans Serif

Colors
f8d9e8
fbd3d4
f59195
e34297
e567a6
eea4c8

Requirements
Must have
• a breast cancer awareness ribbon, the falconridge logo. Clear and simple -impactful.
Nice to have
• If it works with your design and is impactful, add images of athletic girls in action. Not essential. The most important thing is that the call to action is compelling.

```html
<!DOCTYPE html>
<html lang="en">
<head>
<meta charset="utf-8">
<title>Falconridge – Breast Cancer Awareness Campaign Banner</title>
<link rel="stylesheet" href="https://fonts.googleapis.com/css2?family=Open+Sans:wght@400;600;700&display=swap">
<style>
  :root {
    --pink-deep: #e34297;
    --pink-mid: #e567a6;
    --pink-soft: #eea4c8;
    --pink-blush: #f8d9e8;
    --ribbon: #f0a9cf;
    --ribbon-shade: #d97fb2;
    --white: #ffffff;
    --photo-sun: #f3ead0;
    --photo-green: #7f9a55;
    --photo-shadow: #4d5b34;
    --photo-skin: #d9a88a;
  }
  * { margin: 0; padding: 0; box-sizing: border-box; }
  html, body { width: 1200px; height: 591px; overflow: hidden; background: var(--white); }
  .banner {
    position: relative;
    width: 1200px;
    height: 591px;
    overflow: hidden;
    background: linear-gradient(100deg, var(--pink-deep) 0%, var(--pink-mid) 45%, var(--pink-deep) 100%);
    font-family: "Open Sans", sans-serif;
  }
  .banner-bands { position: absolute; inset: 0; }
  .campaign-photo {
    position: absolute;
    left: 0;
    top: 140px;
    width: 800px;
    height: 410px;
    background: linear-gradient(90deg,
      var(--photo-green) 0%,
      var(--photo-sun) 18%,
      var(--photo-skin) 34%,
      var(--photo-green) 48%,
      var(--photo-shadow) 60%,
      rgba(200, 90, 150, 0.8) 76%,
      rgba(227, 66, 151, 0) 100%);
  }
  .logo-plate {
    position: absolute;
    left: 0;
    top: 0;
    width: 366px;
    height: 128px;
    background: var(--white);
    clip-path: polygon(0 0, 100% 0, 90% 100%, 0 100%);
    display: flex;
    align-items: center;
    padding-left: 26px;
  }
  .logo-name {
    font-size: 40px;
    font-weight: 700;
    color: var(--pink-deep);
    line-height: 1;
  }
  .awareness-ribbon {
    position: absolute;
    left: 78px;
    top: 410px;
    width: 90px;
    height: 158px;
  }
  .campaign-copy {
    position: absolute;
    right: 48px;
    top: 0;
    width: 600px;
    height: 460px;
    color: var(--white);
    text-align: right;
  }
  .copy-line { position: absolute; right: 0; white-space: nowrap; font-weight: 400; line-height: 1; }
  .copy-line strong { font-weight: 600; }
  .line-start    { top: 77px;  font-size: 31px; }
  .line-duration { top: 119px; font-size: 31px; }
  .line-goal     { top: 166px; font-size: 39px; }
  .line-raise    { top: 222px; font-size: 39px; }
  .line-cause    { top: 282px; font-size: 37px; }
  .line-cta      { top: 346px; font-size: 88px; }
</style>
</head>
<body>
<main class="banner">
  <svg class="banner-bands" width="1200" height="591" viewBox="0 0 1200 591" aria-hidden="true">
    <polygon points="330,0 745,0 705,42 300,42" fill="var(--pink-soft)" opacity="0.75"/>
    <polygon points="745,0 1200,0 1200,10 735,10" fill="var(--pink-mid)" opacity="0.6"/>
    <polygon points="400,591 440,548 1200,505 1200,591" fill="var(--pink-soft)" opacity="0.7"/>
    <polygon points="0,128 330,128 320,140 0,140" fill="var(--pink-blush)" opacity="0.9"/>
  </svg>

  <div class="campaign-photo" role="img" aria-label="Photo of a smiling teen girl jogging on a sunny park path in a black sports bra"></div>

  <div class="logo-plate">
    <span class="logo-name">Falconridge</span>
  </div>

  <svg class="awareness-ribbon" viewBox="0 0 100 162" aria-label="Pink breast cancer awareness ribbon" role="img">
    <path d="M50 62 C 30 40, 28 14, 50 6 C 72 14, 70 40, 50 62 Z" fill="none" stroke="var(--ribbon)" stroke-width="14" stroke-linejoin="round"/>
    <path d="M40 50 L 12 150 L 28 158 L 56 72 Z" fill="var(--ribbon)"/>
    <path d="M60 50 L 88 150 L 72 158 L 44 72 Z" fill="var(--ribbon-shade)"/>
  </svg>

  <section class="campaign-copy">
    <p class="copy-line line-start">Starting <strong>October 17th</strong></p>
    <p class="copy-line line-duration">A two week campaign</p>
    <p class="copy-line line-goal">To sell <strong>2,500 bras</strong></p>
    <p class="copy-line line-raise">To raise <strong>$25,000</strong></p>
    <p class="copy-line line-cause">For <strong>Breast Bancer</strong></p>
    <p class="copy-line line-cta">Let's do it!</p>
  </section>
</main>
</body>
</html>
```